Business cards and stationary for accounting firm
Marcus Tove
Simple
Public Accountants
PO Box 947, Stn C
Nanaimo, BC
V8T 2M4
info@marcustove.example
marcustove.example
Don't have specific address or phone number yet - this is more about formatting and layout.
Suggestions welcome - possibly one side solely logo and other side address & contact info?

```html
<!DOCTYPE html>
<html lang="en">
<head>
<meta charset="utf-8">
<title>Marcus Tove — Stationery Set</title>
<link href="https://fonts.googleapis.com/css2?family=Open+Sans:wght@400;600&display=swap" rel="stylesheet">
<style>
  :root {
    --stage: #2b2b2b;
    --paper: #ffffff;
    --green: #3f8f1f;
    --green-dark: #2b6a12;
    --green-light: #7dbb3f;
    --silver: #c9cfc4;
    --ink: #555b52;
    --watermark: #eef3ea;
  }
  * { margin: 0; padding: 0; box-sizing: border-box; }
  html, body { width: 1200px; height: 636px; overflow: hidden; background: var(--stage); }
  body { position: relative; font-family: "Open Sans", sans-serif; color: var(--ink); }

  .sheet { position: absolute; background: var(--paper); overflow: hidden; box-shadow: 0 3px 10px rgba(0,0,0,.45); }
  .wave { position: absolute; left: 0; bottom: 0; width: 100%; display: block; }

  .brand { position: absolute; display: flex; align-items: center; gap: 6px; }
  .brand-dot { border-radius: 50%; background: var(--green); flex: none; }
  .brand-name { font-weight: 600; color: var(--green); text-transform: uppercase; letter-spacing: .06em; line-height: 1; }
  .brand-tag { font-size: 4px; letter-spacing: .15em; text-transform: uppercase; color: var(--ink); margin-top: 2px; }

  .small { font-size: 4.5px; line-height: 1.5; }

  /* business card front */
  .card-front { left: 38px; top: 199px; width: 173px; height: 89px; }
  .card-front .brand { left: 8px; top: 8px; }
  .card-front .brand-dot { width: 11px; height: 11px; }
  .card-front .brand-name { font-size: 8px; }
  .card-front .person { position: absolute; left: 20px; top: 28px; }
  .card-front .contact { position: absolute; left: 96px; top: 28px; }
  .card-front .wave { height: 30px; }

  /* business card back */
  .card-back { left: 38px; top: 300px; width: 173px; height: 91px;
    background: linear-gradient(180deg, var(--green-light), var(--green) 45%, var(--green-dark)); }
  .card-back .center-dot { position: absolute; left: 77px; top: 30px; width: 20px; height: 20px; border-radius: 50%;
    background: var(--paper); border: 2px solid var(--green-light); }
  .card-back .url { position: absolute; left: 0; right: 0; bottom: 9px; text-align: center; color: #eaf4e0; font-size: 4.5px; letter-spacing: .08em; }

  /* letterhead */
  .letterhead { left: 233px; top: 72px; width: 434px; height: 516px; }
  .letterhead .brand { left: 22px; top: 18px; }
  .letterhead .brand-dot { width: 20px; height: 20px; }
  .letterhead .brand-name { font-size: 14px; }
  .letterhead .brand-tag { font-size: 5px; }
  .letterhead .watermark { position: absolute; left: 117px; top: 170px; width: 186px; height: 186px; border-radius: 50%;
    background: var(--watermark); }
  .letterhead .contact { position: absolute; left: 220px; top: 366px; font-size: 5px; line-height: 1.5; }
  .letterhead .wave { height: 90px; }

  /* envelope back */
  .envelope-back { left: 679px; top: 144px; width: 497px; height: 204px; }
  .envelope-back .flap { position: absolute; inset: 0; width: 100%; height: 100%; }
  .envelope-back .flap-dot { position: absolute; width: 26px; height: 26px; border-radius: 50%; background: var(--green);
    border: 2px solid var(--green-light); left: 235px; }
  .envelope-back .flap-dot.top { top: 16px; }
  .envelope-back .flap-dot.seal { top: 127px; background: var(--paper); border-color: var(--paper); }
  .envelope-back .flap-dot.seal::after { content: ""; position: absolute; inset: 4px; border-radius: 50%; background: var(--green-light); }

  /* envelope front */
  .envelope-front { left: 679px; top: 360px; width: 497px; height: 204px; }
  .envelope-front .brand { left: 14px; top: 14px; }
  .envelope-front .brand-dot { width: 18px; height: 18px; }
  .envelope-front .brand-name { font-size: 13px; }
  .envelope-front .return-address { position: absolute; left: 34px; top: 48px; font-size: 4.5px; line-height: 1.5; }
  .envelope-front .wave { height: 70px; }
  .envelope-front .url { position: absolute; right: 16px; bottom: 8px; color: #eaf4e0; font-size: 4.5px; letter-spacing: .08em; }
</style>
</head>
<body>

<svg width="0" height="0" style="position:absolute" aria-hidden="true">
  <defs>
    <linearGradient id="greenFill" x1="0" y1="0" x2="0" y2="1">
      <stop offset="0" stop-color="#7dbb3f"/>
      <stop offset=".5" stop-color="#3f8f1f"/>
      <stop offset="1" stop-color="#2b6a12"/>
    </linearGradient>
    <symbol id="swoosh" viewBox="0 0 400 100" preserveAspectRatio="none">
      <path d="M0,40 C120,80 260,0 400,14 L400,26 C260,12 120,92 0,52 Z" fill="#c9cfc4"/>
      <path d="M0,58 C120,96 260,18 400,34 L400,100 L0,100 Z" fill="url(#greenFill)"/>
      <path d="M0,58 C120,96 260,18 400,34 L400,38 C260,24 120,100 0,64 Z" fill="#a9d46c"/>
    </symbol>
  </defs>
</svg>

<!-- Business card, front -->
<section class="sheet card-front">
  <div class="brand">
    <span class="brand-dot"></span>
    <div><div class="brand-name">Marcus Tove</div><div class="brand-tag">Public Accountants</div></div>
  </div>
  <div class="person small">
    <div>Marcus Tove</div>
    <div>Principal</div>
  </div>
  <div class="contact small">
    <div>PO Box 947, Stn C</div>
    <div>Nanaimo, BC V8T 2M4</div>
    <div>T 250.555.0100</div>
    <div>info@marcustove.example</div>
  </div>
  <svg class="wave" aria-hidden="true"><use href="#swoosh"/></svg>
</section>

<!-- Business card, back -->
<section class="sheet card-back">
  <span class="center-dot"></span>
  <div class="url">marcustove.example</div>
</section>

<!-- Letterhead -->
<section class="sheet letterhead">
  <div class="brand">
    <span class="brand-dot"></span>
    <div><div class="brand-name">Marcus Tove</div><div class="brand-tag">Public Accountants</div></div>
  </div>
  <span class="watermark"></span>
  <div class="contact">
    <div>PO Box 947, Stn C</div>
    <div>Nanaimo, BC</div>
    <div>V8T 2M4</div>
    <div>T 250.555.0100</div>
    <div>info@marcustove.example</div>
    <div>marcustove.example</div>
  </div>
  <svg class="wave" aria-hidden="true"><use href="#swoosh"/></svg>
</section>

<!-- Envelope, back -->
<section class="sheet envelope-back">
  <svg class="flap" viewBox="0 0 497 204" preserveAspectRatio="none" aria-hidden="true">
    <path d="M0,70 C140,125 250,125 497,62 L497,204 L0,204 Z" fill="url(#greenFill)"/>
    <path d="M0,70 C140,125 250,125 497,62 L497,68 C250,131 140,131 0,76 Z" fill="#a9d46c"/>
    <path d="M0,60 C140,113 250,113 497,52 L497,58 C250,119 140,119 0,66 Z" fill="#c9cfc4"/>
  </svg>
  <span class="flap-dot top"></span>
  <span class="flap-dot seal"></span>
</section>

<!-- Envelope, front -->
<section class="sheet envelope-front">
  <div class="brand">
    <span class="brand-dot"></span>
    <div><div class="brand-name">Marcus Tove</div><div class="brand-tag">Public Accountants</div></div>
  </div>
  <div class="return-address">
    <div>PO Box 947, Stn C</div>
    <div>Nanaimo, BC</div>
    <div>V8T 2M4</div>
  </div>
  <svg class="wave" aria-hidden="true"><use href="#swoosh"/></svg>
  <div class="url">marcustove.example</div>
</section>

</body>
</html>
```